Business card design needed

We are a unique and exciting Drama, Dance and Fitness studio that offers classes from 18 months to adults - with a strong focus on the Under 5's market and we mainly cater for children under 14 years. We aim to create confidence in ALL of our students. We have a very happy and encouraging environment at our studio so would like my business card to 'project this'. I would like my 'catchphrase' - "Building Brilliance" - It's your moment to GLOW! to be on the front of my business card also.

Myself as the Principal has a VERY bubbly personality - so I need this business card to project this also. Stars(silver?) and perhaps pictures/silouettes of happy children would be appropriate. And as we also have adult fitness classes, pictures/silouettes of adults in yoga poses/exercise poses would be nice to have too. We are a very 'theatrical' school so would like my business card to look as 'exciting' as possible - but incorporating my school colours of red, royal blue, silver and white.
Updates

                                       

Hi everyone - thankyou so far for your designs.  I feel like I need to show a bit more 'excitement' with the business cards that I have seen so far.  I would definitely like to see stars(preferably silver) on there, and preferably pictures/silhouettes of children happy/performing.  If you can fit pictures/silouettes of adults exercising - yoga/zumba etc that would be a bonus.  I have got an extremely bubbly, theatrical personality, so I need that to be reflected with my name and title on the card also. The colour scheme of my colours red, royal blue, silver and white is a priority too and most of you have done this.  Thankyou.                                   

Target Market(s)

Families with children - especially those who love to perform, and for adults who like to exercise.

Industry/Entity Type

Environment

Contact Information for Business Card

Marisol's Footlight Flyers - Drama Dance Performance and Fitness Studio. Unit 4, 58 Larkspur Rd KESTREL JUNCTION. "Building Brilliance" - It's your moment to GLOW! Marisol Venkley PRINCIPAL. Phone: 0427 395160 Email: brightkids@pelnet.com.au Web: www.marisolsfootlightflyers.com.au

Requirements
Must have
• Our studio colours are Red, Royal Blue with a bit of silver and white. I also LOVE stars - and this would suit my business card. Also need to have my logo on there - which I have uploaded. I would like my 'catchphrase' - "Building Brilliance" - It's your moment to GLOW! to be on the front of my business card also.
Nice to have
• Pictures/silouettes of happy children would be appropriate. And as we also have adult fitness classes, pictures/silouettes of adults in yoga poses/exercise poses would be nice to have too. We are a very 'theatrical' school so would like my business card to look as 'exciting' as possible - but incorporating my school colours of red, royal blue, silver and white.

```html
<!DOCTYPE html>
<html lang="en">
<head>
<meta charset="utf-8">
<title>Marisol's Footlight Flyers — Business Card</title>
<link rel="stylesheet" href="https://fonts.googleapis.com/css2?family=Ubuntu:wght@400;500;700&display=swap">
<style>
  :root {
    --canvas-bg: #ece9e4;
    --red-light: #c8202f;
    --red-mid: #a01824;
    --red-dark: #6e0d15;
    --white: #ffffff;
    --card-white: #f7f7f8;
    --royal-blue: #1f3b8f;
    --navy: #1d2a5c;
    --ink: #1a1a1a;
    --shadow: rgba(0, 0, 0, 0.28);
  }
  * { box-sizing: border-box; margin: 0; padding: 0; }
  html, body {
    width: 1200px;
    height: 1000px;
    overflow: hidden;
    background: var(--canvas-bg);
    font-family: "Ubuntu", Arial, sans-serif;
  }
  .card-sheet {
    position: relative;
    width: 1200px;
    height: 1000px;
  }
  .card {
    position: absolute;
    top: 348px;
    width: 537px;
    height: 303px;
    border-radius: 14px;
    overflow: hidden;
    box-shadow: 0 6px 16px var(--shadow);
  }
  .card--front { left: 45px; background: var(--card-white); }
  .card--back {
    left: 618px;
    background: radial-gradient(ellipse at 50% 35%, var(--red-light) 0%, var(--red-mid) 55%, var(--red-dark) 100%);
  }
  .star-texture {
    position: absolute;
    inset: 0;
  }
  .card--front .star-texture { background: linear-gradient(180deg, #fafafb 0%, #eff0f2 100%); }
  .front-panel {
    position: absolute;
    inset: 0;
    width: 537px;
    height: 303px;
  }
  .brand {
    position: absolute;
    text-align: center;
    white-space: nowrap;
  }
  .brand__name {
    font-weight: 700;
    line-height: 1;
  }
  .brand__tagline {
    font-weight: 700;
    color: var(--ink);
    line-height: 1;
    margin-top: 6px;
  }
  .card--front .brand { left: 30px; top: 36px; width: 200px; }
  .card--front .brand__name { font-size: 17px; color: var(--royal-blue); }
  .card--front .brand__tagline { font-size: 8.4px; }
  .person {
    position: absolute;
    left: 20px;
    top: 155px;
    width: 220px;
    text-align: center;
    white-space: nowrap;
  }
  .person__name {
    font-size: 20px;
    font-weight: 500;
    color: var(--red-light);
  }
  .person__title {
    margin-top: 10px;
    font-size: 14px;
    font-weight: 500;
    letter-spacing: 3px;
    color: var(--navy);
  }
  .contact-list {
    position: absolute;
    left: 305px;
    top: 100px;
    list-style: none;
    color: var(--white);
    font-size: 11px;
    white-space: nowrap;
  }
  .contact-list li {
    display: flex;
    align-items: flex-start;
    gap: 7px;
    margin-bottom: 9px;
    line-height: 1.2;
  }
  .contact-list svg { flex: none; width: 17px; height: 17px; }
  .contact-list span { padding-top: 2px; }
  .card--back .brand { left: 0; right: 0; top: 130px; }
  .card--back .brand__name { font-size: 22px; color: var(--white); }
  .card--back .brand__tagline { font-size: 9.5px; color: var(--white); }
  .catchphrase {
    position: absolute;
    left: 0;
    right: 0;
    bottom: 16px;
    text-align: center;
    color: var(--white);
    font-size: 18px;
    font-weight: 500;
    white-space: nowrap;
  }
</style>
</head>
<body>
<main class="card-sheet">

  <section class="card card--front" aria-label="Card front">
    <div class="star-texture" role="img" aria-label="Faint silver star pattern on white"></div>
    <svg class="front-panel" viewBox="0 0 537 303" aria-hidden="true">
      <defs>
        <linearGradient id="redPanel" x1="0" y1="0" x2="1" y2="0">
          <stop offset="0" stop-color="#c8202f"/>
          <stop offset="0.5" stop-color="#a01824"/>
          <stop offset="1" stop-color="#6e0d15"/>
        </linearGradient>
      </defs>
      <path d="M250 0 C295 40 280 120 274 170 C268 230 266 270 276 303 L537 303 L537 0 Z" fill="url(#redPanel)"/>
      <path d="M262 0 C306 40 290 120 284 170 C278 230 276 270 286 303" fill="none" stroke="#ffffff" stroke-width="1.5"/>
    </svg>

    <div class="brand">
      <p class="brand__name">Marisol's Footlight Flyers</p>
      <p class="brand__tagline">Drama Dance Performance and Fitness Studio</p>
    </div>

    <div class="person">
      <p class="person__name">Marisol Venkley</p>
      <p class="person__title">principal</p>
    </div>

    <ul class="contact-list">
      <li>
        <svg viewBox="0 0 20 20"><circle cx="10" cy="10" r="9" fill="none" stroke="#fff" stroke-width="1.6"/><path d="M7 5.5l1.6 2.2-1 1.2c.6 1.3 1.5 2.2 2.8 2.8l1.2-1 2.2 1.6-.9 1.8c-3.7-.4-6.4-3.1-6.8-6.8z" fill="#fff"/></svg>
        <span>0427 395160</span>
      </li>
      <li>
        <svg viewBox="0 0 20 20"><circle cx="10" cy="10" r="9" fill="none" stroke="#fff" stroke-width="1.6"/><path d="M5 7l5 3.5 5-3.5v6.5H5z" fill="#fff"/></svg>
        <span>brightkids@pelnet.com.au</span>
      </li>
      <li>
        <svg viewBox="0 0 20 20"><circle cx="10" cy="10" r="9" fill="none" stroke="#fff" stroke-width="1.6"/><path d="M10 4.5l5.5 5h-1.8v5H6.3v-5H4.5z" fill="#fff"/></svg>
        <span>Unit 4, 58 Larkspur Rd<br>KESTREL JUNCTION</span>
      </li>
      <li>
        <svg viewBox="0 0 20 20"><circle cx="10" cy="10" r="8.5" fill="#fff"/><g fill="none" stroke="#a01824" stroke-width="1"><ellipse cx="10" cy="10" rx="3.2" ry="8"/><path d="M2 10h16M3.5 6h13M3.5 14h13"/></g></svg>
        <span>www.marisolsfootlightflyers.com.au</span>
      </li>
    </ul>
  </section>

  <section class="card card--back" aria-label="Card back">
    <div class="star-texture" role="img" aria-label="Faint star pattern over red gradient"></div>
    <div class="brand">
      <p class="brand__name">Marisol's Footlight Flyers</p>
      <p class="brand__tagline">Drama Dance Performance and Fitness Studio</p>
    </div>
    <p class="catchphrase">"Building Brilliance" - It's your moment to GLOW!</p>
  </section>

</main>
</body>
</html>
```